Redesign Business Cards, Attached

Please read instructions carefully. If you have any questions send a message before submitting your ONE design. Please redesign attached business cards. Double sided. Use same content and descriptions. Use black, silver, crimson red and gold colors. My only issue with the attached design is the background colors. I like the layout as-is. I can provide the individual pictures on the back side later. Do not submit more than one design. One submission shall include both front and back. Do not submit front and back separately. A second project will be launched to create a matching post card after completion of this.
Industry/Entity Type
see description and attachments.
Contact Information for Business Card
Requirements
Must have
- see description and attachments.
Nice to have
Should not have

```html
<!DOCTYPE html>
<html lang="en">
<head>
<meta charset="UTF-8">
<title>Harbor Helm – Business Card, Front and Back</title>
<link href="https://fonts.googleapis.com/css2?family=Montserrat:wght@400;700;800&family=Poppins:wght@700&display=swap" rel="stylesheet">
<style>
  :root {
    --page-bg: #2b2d30;
    --card-black: #111113;
    --card-black-soft: #1c1c20;
    --crimson: #a4162d;
    --gold: #d9a92b;
    --silver: #c9cdd2;
    --silver-light: #eef0f2;
    --steel: #6f7780;
  }
  * { box-sizing: border-box; margin: 0; padding: 0; }
  html, body {
    width: 1200px;
    height: 1200px;
    overflow: hidden;
    background: var(--page-bg);
  }
  .sheet {
    width: 1200px;
    height: 1200px;
    display: flex;
    flex-direction: column;
    align-items: center;
    justify-content: center;
    gap: 60px;
  }
  .card {
    position: relative;
    width: 900px;
    height: 514px;
    border-radius: 34px;
    background: linear-gradient(135deg, var(--card-black-soft) 0%, var(--card-black) 70%);
    overflow: hidden;
    box-shadow: 0 18px 40px rgba(0,0,0,0.5);
  }

  /* Brand: plain circle + name */
  .brand {
    position: absolute;
    display: flex;
    align-items: center;
    gap: 14px;
  }
  .brand-dot {
    width: 54px;
    height: 54px;
    border-radius: 50%;
    background: var(--silver);
    flex: none;
  }
  .brand-name {
    font-family: "Montserrat", sans-serif;
    font-weight: 700;
    font-size: 17px;
    line-height: 1.25;
    letter-spacing: 0.06em;
    text-transform: uppercase;
    color: var(--gold);
  }

  /* Front */
  .card-front .brand { top: 52px; right: 56px; }
  .holder {
    position: absolute;
    left: 90px;
    top: 200px;
  }
  .holder-name {
    font-family: "Montserrat", sans-serif;
    font-weight: 800;
    font-size: 44px;
    letter-spacing: 0.02em;
    color: var(--gold);
    text-transform: uppercase;
  }
  .holder-title {
    margin-top: 6px;
    padding-left: 24px;
    font-family: "Montserrat", sans-serif;
    font-weight: 400;
    font-size: 27px;
    line-height: 1.3;
    color: var(--silver-light);
  }
  .front-rule {
    position: absolute;
    left: 120px;
    right: 30px;
    top: 338px;
    height: 2px;
    background: var(--crimson);
  }
  .contacts {
    position: absolute;
    left: 120px;
    top: 360px;
    list-style: none;
  }
  .contacts li {
    display: flex;
    align-items: center;
    gap: 22px;
    height: 40px;
    font-family: "Montserrat", sans-serif;
    font-weight: 400;
    font-size: 26px;
    color: var(--silver);
  }
  .contacts svg { width: 26px; height: 26px; flex: none; }

  /* Back */
  .card-back .brand { top: 48px; left: 52px; }
  .sea-photo {
    position: absolute;
    top: 0;
    right: 0;
    width: 58%;
    height: 100%;
    background:
      radial-gradient(ellipse at 72% 35%, rgba(238,240,242,0.85) 0%, rgba(201,205,210,0.45) 28%, rgba(111,119,128,0) 62%),
      linear-gradient(90deg, var(--card-black) 0%, #2a2d31 30%, var(--steel) 65%, var(--silver) 100%);
  }
  .services {
    position: absolute;
    left: 60px;
    top: 190px;
    list-style: none;
    font-family: "Poppins", sans-serif;
    font-weight: 700;
    font-size: 29px;
    line-height: 1.28;
    color: var(--gold);
    text-shadow: 0 1px 3px rgba(0,0,0,0.55);
  }
  .services li::before { content: "• "; }
  .services li.continued { padding-left: 20px; }
  .services li.continued::before { content: ""; }
</style>
</head>
<body>
<main class="sheet">

  <section class="card card-front">
    <div class="brand">
      <span class="brand-dot"></span>
      <span class="brand-name">Harbor Helm<br>Boat Training &amp; Charters</span>
    </div>

    <div class="holder">
      <h1 class="holder-name">Jordan T. Halvers</h1>
      <p class="holder-title">USCG Licensed Captain<br>Certified Instructor</p>
    </div>

    <div class="front-rule"></div>

    <ul class="contacts">
      <li>
        <svg viewBox="0 0 24 24"><path fill="var(--gold)" d="M6.6 10.8a15.1 15.1 0 0 0 6.6 6.6l2.2-2.2a1 1 0 0 1 1-.25 11.4 11.4 0 0 0 3.6.57 1 1 0 0 1 1 1V20a1 1 0 0 1-1 1A17 17 0 0 1 3 4a1 1 0 0 1 1-1h3.5a1 1 0 0 1 1 1c0 1.25.2 2.45.57 3.57a1 1 0 0 1-.25 1z"/></svg>
        (555) 014-2739
      </li>
      <li>
        <svg viewBox="0 0 24 24"><path fill="var(--gold)" d="M2 5h20v14H2z"/><path fill="none" stroke="var(--card-black)" stroke-width="1.6" d="M2 5l10 8 10-8"/></svg>
        hello@harborhelm.com
      </li>
      <li>
        <svg viewBox="0 0 24 24" fill="none" stroke="var(--gold)" stroke-width="2"><circle cx="12" cy="12" r="9.5"/><path d="M2.5 12h19M12 2.5c3 3 3 16 0 19M12 2.5c-3 3-3 16 0 19"/></svg>
        www.HarborHelm.com
      </li>
    </ul>
  </section>

  <section class="card card-back">
    <div class="sea-photo" role="img" aria-label="Photo of a white center-console boat speeding across sparkling water"></div>

    <div class="brand">
      <span class="brand-dot"></span>
      <span class="brand-name">Harbor Helm<br>Boat Training &amp; Charters</span>
    </div>

    <ul class="services">
      <li>Boat Training • To Power boating</li>
      <li>Docking &amp; Boat Handling</li>
      <li>Boat Handling • Island Anchoring</li>
      <li>Open Water Advanced Maneuvers</li>
      <li>Coastal Navigation</li>
      <li>Captaining/Piloting Service</li>
      <li class="continued">for Your Outings</li>
    </ul>
  </section>

</main>
</body>
</html>
```